Webdesign for Non profit Diabetes education company

We are looking for a website design for our company.

We just created the company Glucose Guidance Circle

The concept for the company is to educate diabetics with resources that will help them manage their Diabetes. The list of advisers will be dietitians, podiatrist, diabetic educators, and fitness centers.

Please see attached logo. I like the logo to include an image that connects people together.

I've attached our logo, please use the colors in the design of the site.

Creativity is encouraged. Have fun with this project. We are looking for a professional site but not to corporate.

The page must be written in HTML 5 and be responsive built for mobile. You can use bootstrap, jquery, or angular JS.

Wordpress or wix will not be accepted.

The website will be hosted at www.glucoseguidancecircle.example

Requirements
Must have
• The page must be written in HTML 5 and be responsive built for mobile. You can use bootstrap, jquery, or angular JS.
• The landing page should include a splash page. Please incorporate the logo and the
Should not have
• Wordpress or wix will not be accepted.

```html
<!DOCTYPE html>
<html lang="en">
<head>
<meta charset="utf-8">
<title>Glucose Guidance Circle</title>
<link rel="stylesheet" href="https://fonts.googleapis.com/css2?family=Arimo:wght@400;500;700&display=swap">
<style>
:root{
  --pink:#ff5f8a;
  --blue:#6b8fcf;
  --ink:#222;
  --muted:#444;
  --nav-bg:#f3f3f3;
  --hero-top:#f0f0f0;
  --hero-bottom:#fafafa;
  --art-a:#eef1f6;
  --art-b:#f1e9ea;
}
*{margin:0;padding:0;box-sizing:border-box}
html,body{width:1200px;height:1200px;overflow:hidden;background:#fff}
body{position:relative;font-family:"Arimo",Arial,sans-serif;color:var(--ink)}
.social{position:absolute;top:23px;left:502px;display:flex;gap:15px}
.social span{width:39px;height:39px;border:2px solid #555;border-radius:50%}
.site-nav{position:absolute;left:36px;top:85px;width:1137px;height:97px;background:var(--nav-bg);border-bottom:4px solid var(--pink)}
.brand{position:absolute;left:28px;top:22px;display:flex;align-items:center;gap:12px;color:var(--pink);font-size:22px;font-weight:700}
.brand i{width:44px;height:44px;border:5px solid var(--blue);border-radius:50%}
.nav-links{position:absolute;right:0;top:0;height:93px;display:flex;align-items:center;font-size:21px;color:#333}
.nav-links a{color:inherit;text-decoration:none;padding:0 30px;height:93px;line-height:93px}
.nav-links a.active{background:var(--pink);color:#fff;padding:0 31px}
.hero{position:absolute;left:36px;top:182px;width:1136px;height:518px;background:linear-gradient(var(--hero-top),var(--hero-bottom))}
.care-art{position:absolute;left:84px;top:88px;width:700px;height:356px;border-radius:14px;background:linear-gradient(100deg,var(--art-a),var(--art-b))}
.care-label{position:absolute;font-size:13.5px;font-weight:700;color:#333;white-space:nowrap}
.hero-brand{position:absolute;left:800px;top:135px;width:300px;text-align:center}
.hero-brand i{display:block;width:130px;height:130px;margin:0 auto 20px;border:12px solid var(--blue);border-radius:50%}
.hero-brand span{display:block;color:var(--pink);font-size:38px;font-weight:700;line-height:1.1}
.mission{position:absolute;left:34px;top:700px;width:1137px;height:129px;background:var(--pink);color:#fff;padding:31px 30px 0;font-size:19.5px;font-weight:700;line-height:24px;text-transform:uppercase;letter-spacing:-.2px}
.definition{position:absolute;left:64px;top:873px;width:1110px;font-size:23.5px;font-weight:400;line-height:27px;text-transform:uppercase;text-decoration:underline;text-underline-offset:4px}
.stat{position:absolute;top:970px;width:220px}
.stat svg{display:block}
.stat .value{position:absolute;left:0;top:0;width:194px;height:194px;display:flex;align-items:center;justify-content:center;font-size:21px;font-weight:500;color:#333}
.stat .label{margin-top:8px;font-size:23px;font-weight:700;color:var(--muted)}
.stat-total{left:64px}.stat-diagnosed{left:468px}.stat-undiagnosed{left:846px}
</style>
</head>
<body>
<div class="social" aria-label="Social links"><span></span><span></span><span></span><span></span></div>

<header class="site-nav">
  <div class="brand"><i></i>Glucose Guidance Circle</div>
  <nav class="nav-links">
    <a class="active" href="#">Home</a>
    <a href="#">Find Healthcare Provider</a>
    <a href="#">Blog</a>
  </nav>
</header>

<section class="hero">
  <div class="care-art" role="img" aria-label="Illustration of a caregiver with an elderly woman beside a care path linking a pedorthist, diabetic educator, endocrinologist, nutritionists and podiatrist"></div>
  <span class="care-label" style="left:260px;top:196px">PEDORTHIST</span>
  <span class="care-label" style="left:327px;top:424px">DIABETIC EDUCATOR</span>
  <span class="care-label" style="left:413px;top:89px">ENDOCRINOLOGIST</span>
  <span class="care-label" style="left:620px;top:88px">PODIATRIST</span>
  <span class="care-label" style="left:525px;top:398px">NUTRITIONISTS</span>
  <div class="hero-brand"><i></i><span>Glucose Guidance Circle</span></div>
</section>

<section class="mission">“At the Glucose Guidance Circle, our focus is to connect newly diagnosed and existing patients with diabetes to a network of available professionals&nbsp; who possess the knowledge to manage your diabetes.”</section>

<h1 class="definition">Diabetes occurs when your blood glucose, also called blood sugar, is too high. High blood glucose can cause health problems over time.</h1>

<div class="stat stat-total">
  <svg width="194" height="194" viewBox="0 0 194 194"><circle cx="97" cy="97" r="89" fill="none" stroke="var(--blue)" stroke-width="14"/></svg>
  <div class="value">30.3 MILLION</div>
  <div class="label">Total</div>
</div>
<div class="stat stat-diagnosed">
  <svg width="194" height="194" viewBox="0 0 194 194">
    <circle cx="97" cy="97" r="89" fill="none" stroke="var(--blue)" stroke-width="14"/>
    <path d="M111 9 A89 89 0 0 1 163 38" fill="none" stroke="var(--pink)" stroke-width="14"/>
  </svg>
  <div class="value">23.1 MILLION</div>
  <div class="label">Diagnosed</div>
</div>
<div class="stat stat-undiagnosed">
  <svg width="194" height="194" viewBox="0 0 194 194">
    <circle cx="97" cy="97" r="89" fill="none" stroke="var(--pink)" stroke-width="14"/>
    <path d="M111 9 A89 89 0 0 1 163 38" fill="none" stroke="var(--blue)" stroke-width="14"/>
  </svg>
  <div class="value">7.2 MILLION</div>
  <div class="label">Undiagnosed</div>
</div>
</body>
</html>
```